" Cavalto Solutions oferece serviços de automação de tarefas manuais repetitivas realizadas na administração das empresas, como ingresso de faturas, coleta de dados de vários sistemas e consolidação manual, aceso a site para extração de dados e posterior registro em sistemas próprios, etc. Os serviços que oferece são: a identificação dessas oportunidades apoiando no budiness case, o desenvolvimento dos robôs para automação, a implantação do modelo de governança para assegurar a boa implantação e posterior sustentabilidade, transferência de conhecimento para as equipes internos, e finalmente o suporte e manutenção da plataforma. "

```html
<!DOCTYPE html>
<html lang="pt-BR">
<head>
<meta charset="UTF-8">
<title>Cavalto Solutions — Automação com RPA</title>
<link href="https://fonts.googleapis.com/css2?family=Open+Sans:wght@400;600;700;800&display=swap" rel="stylesheet">
<style>
  :root {
    --ink: #1b2b4d;
    --brand: #1e9fd6;
    --white: #ffffff;
    --navy-deep: #0b2447;
    --navy-mid: #163a68;
    --photo-light: #cdd8e0;
    --photo-mid: #7d93a6;
    --photo-dark: #2a3b4f;
  }
  * { margin: 0; padding: 0; box-sizing: border-box; }
  html, body { width: 1200px; height: 1200px; overflow: hidden; }
  body {
    font-family: "Open Sans", Arial, sans-serif;
    background: var(--white);
    position: relative;
  }
  .site-header {
    position: absolute; left: 0; top: 0;
    width: 1200px; height: 228px;
    background: var(--white);
    border-bottom: 2px solid #e3e7ec;
  }
  .brand {
    position: absolute; left: 67px; top: 80px;
    display: flex; align-items: center; gap: 22px;
  }
  .brand-mark {
    width: 52px; height: 52px; background: var(--brand);
  }
  .brand-name {
    font-size: 46px; font-weight: 600; color: var(--ink);
    letter-spacing: 1px; line-height: 1;
  }
  .main-nav {
    position: absolute; left: 772px; top: 110px;
    white-space: nowrap;
    font-size: 25px; font-weight: 600; color: var(--ink);
    letter-spacing: 0.5px;
  }
  .main-nav .active { font-weight: 800; }
  .main-nav .sep { margin: 0 10px; font-weight: 400; }

  .hero {
    position: absolute; left: 0; top: 230px;
    width: 1200px; height: 622px;
    overflow: hidden;
  }
  .hero-photo {
    position: absolute; inset: 0;
    background:
      radial-gradient(ellipse at 80% 35%, rgba(190,225,240,0.7), transparent 45%),
      linear-gradient(180deg, var(--photo-light) 0%, var(--photo-mid) 45%, var(--photo-dark) 100%);
  }
  .hero-copy {
    position: absolute; left: 67px; top: 325px;
    color: var(--white);
    white-space: nowrap;
  }
  .hero-title {
    font-size: 40px; font-weight: 700; letter-spacing: 0.5px;
    margin-bottom: 12px;
  }
  .hero-text {
    font-size: 29px; font-weight: 700; line-height: 53px;
  }

  .about {
    position: absolute; left: 0; top: 852px;
    width: 1200px; height: 348px;
    background: linear-gradient(180deg, var(--navy-deep) 0%, var(--navy-mid) 100%);
    color: var(--white);
    padding: 52px 0 0 67px;
    white-space: nowrap;
  }
  .about-title {
    font-size: 33px; font-weight: 700; letter-spacing: 0.5px;
  }
  .about-kicker {
    margin-top: 22px;
    font-size: 26px; font-weight: 400;
  }
  .about-text {
    margin-top: 24px;
    font-size: 27px; font-weight: 400; line-height: 65px;
  }
</style>
</head>
<body>
  <header class="site-header">
    <div class="brand">
      <span class="brand-mark"></span>
      <span class="brand-name">Cavalto Solutions</span>
    </div>
    <nav class="main-nav">
      <span class="active">SOBRE NÓS</span><span class="sep">|</span>SAIBA MAIS<span class="sep">|</span>QUEM
    </nav>
  </header>

  <section class="hero">
    <div class="hero-photo" role="img" aria-label="Fotografia de um profissional tocando uma interface digital futurista com gráficos de automação"></div>
    <div class="hero-copy">
      <h1 class="hero-title">AUTOMAÇÃO COM RPA</h1>
      <p class="hero-text">
        Implantação de RPA -&nbsp; Robotic Process Automation com metodologias ágeis<br>
        que garantem o foco na rápida entrega de valor para o negocio,<br>
        utilizando aceleradores e ferramentas para ser mais assertivo na escolha de<br>
        processos candidatos e reduzir o tempo de desenvolvimento.
      </p>
    </div>
  </section>

  <section class="about">
    <h2 class="about-title">: : QUEM SOMOS</h2>
    <p class="about-kicker">SEU PARCEIRO DE RPA</p>
    <p class="about-text">
      Somos uma empresa com experiência na implantação da força de trabalho virtual,<br>
      oferecendo nossos serviços e soluções para automação com Robotic Process<br>
      Automation (RPA), uma tecnologia usada para otimizar e automatizar Processos.
    </p>
  </section>
</body>
</html>
```